2nd Generation Blind Manufacturer & Retailer Needs A Stationary Set

We need a stationary set for a family business located the in the Whitsundays (QLD). We retail and manufacture blinds awnings and shutters. Second generation, in operation for over 30 years.

Final draft must include at minimum:

Business Card (2 Sided)
Letterhead
Presentation Folder

Target Market(s)

home owners, landlords, builders, real estate agents, shopping centres

Industry/Entity Type

Textile

Requirements
Must have
• Design needs to work in mono as well as colour print
Nice to have
• Relevant to the textile industry
Should not have
• The inclusion of blinds, awnings or shutters is an automatic no-no

```html
<!DOCTYPE html>
<html lang="en">
<head>
<meta charset="utf-8">
<title>Hartwell Blinds – Business Card</title>
<link href="https://fonts.googleapis.com/css2?family=Tinos:wght@400&display=swap" rel="stylesheet">
<style>
  :root {
    --backdrop: #1d2124;
    --card: #ffffff;
    --panel: #8a8a8a;
    --panel-light: #a3a3a3;
    --brand-grey: #7d7d7d;
    --teal: #1bb5b5;
    --text: #6e6e6e;
    --white: #ffffff;
  }
  * { margin: 0; padding: 0; box-sizing: border-box; }
  html, body { width: 1200px; height: 950px; overflow: hidden; }
  body {
    background: var(--backdrop);
    font-family: "Tinos", "Times New Roman", serif;
    position: relative;
  }
  .card {
    position: absolute;
    width: 640px;
    height: 366px;
    background: var(--card);
    box-shadow: 0 10px 30px rgba(0,0,0,0.45);
  }
  .card--front { left: 120px; top: 70px; display: flex; align-items: center; justify-content: center; }
  .card--back { left: 440px; top: 510px; display: flex; }

  .brand { display: flex; align-items: center; gap: 22px; }
  .brand__mark { width: 78px; height: 78px; background: var(--brand-grey); }
  .brand__name {
    color: var(--brand-grey);
    font-size: 42px;
    line-height: 1;
    letter-spacing: 3px;
    text-transform: uppercase;
  }

  .contact { width: 48%; padding: 68px 0 0 44px; color: var(--text); }
  .contact__name { color: var(--teal); font-size: 25px; letter-spacing: 1.5px; text-transform: uppercase; }
  .contact__role { font-size: 16px; margin-top: 4px; }
  .contact__address { font-size: 15px; line-height: 1.3; margin-top: 36px; }
  .contact__list { list-style: none; margin-top: 16px; font-size: 15px; line-height: 1.45; }
  .contact__list li { display: flex; align-items: center; gap: 10px; }
  .contact__list svg { width: 14px; height: 14px; flex: none; }

  .panel {
    flex: 1;
    background: linear-gradient(135deg, var(--panel-light), var(--panel));
    display: flex;
    align-items: center;
    justify-content: center;
  }
  .panel__name {
    color: var(--white);
    font-size: 44px;
    line-height: 1.05;
    letter-spacing: 3px;
    text-transform: uppercase;
    text-align: left;
  }
</style>
</head>
<body>
  <section class="card card--front" aria-label="Business card front">
    <div class="brand">
      <div class="brand__mark"></div>
      <div class="brand__name">Hartwell<br>Blinds</div>
    </div>
  </section>

  <section class="card card--back" aria-label="Business card back">
    <div class="contact">
      <h1 class="contact__name">Sam Keller</h1>
      <p class="contact__role">President</p>
      <p class="contact__address">2140 Harbour View Road<br>Bayside Park, NY 11020</p>
      <ul class="contact__list">
        <li>
          <svg viewBox="0 0 14 14"><circle cx="7" cy="7" r="7" fill="#1bb5b5"/><path d="M4.3 3.6l1.4-.2.8 1.8-.9.7c.5 1 1.3 1.8 2.3 2.3l.7-.9 1.8.8-.2 1.4c-3.3 0-6-2.7-5.9-5.9z" fill="#fff"/></svg>
          412 6390 1874
        </li>
        <li>
          <svg viewBox="0 0 14 14"><circle cx="7" cy="7" r="7" fill="#1bb5b5"/><rect x="4.8" y="3" width="4.4" height="8" rx="0.8" fill="#fff"/><rect x="5.5" y="4" width="3" height="5" fill="#1bb5b5"/></svg>
          739 2148 6603
        </li>
        <li>
          <svg viewBox="0 0 14 14"><circle cx="7" cy="7" r="7" fill="#1bb5b5"/><rect x="3.5" y="4.5" width="7" height="5" fill="#fff"/><path d="M3.5 4.5L7 7.3l3.5-2.8" fill="none" stroke="#1bb5b5" stroke-width="0.8"/></svg>
          sam@hartwell.com
        </li>
        <li>
          <svg viewBox="0 0 14 14"><circle cx="7" cy="7" r="7" fill="#1bb5b5"/><circle cx="7" cy="7" r="3.6" fill="none" stroke="#fff" stroke-width="0.9"/><path d="M3.4 7h7.2M7 3.4c-1.5 2.2-1.5 5 0 7.2M7 3.4c1.5 2.2 1.5 5 0 7.2" fill="none" stroke="#fff" stroke-width="0.8"/></svg>
          www.hartwell.com
        </li>
      </ul>
    </div>
    <div class="panel">
      <div class="panel__name">Hartwell<br>Blinds</div>
    </div>
  </section>
</body>
</html>
```